vantaline7 - a safety solution for schools

A Amok App for schools needs your help to design some screens. Its important to have a very simple use of the app. The function of the app is very easy, you put the button to trigger the alarm. The app has a message function. So we need 3 howto screens. you find a better description of the project in the briefing-file. If you have any questions just ask. Thanks in advance for the suggestions. Best Regards, Mert

Target Market(s)

Schools

Industry/Entity Type

Security Service

Font styles to use
Sans Serif

Colors

Designer to choose colors to be used in the design.

Requirements
Must have
• Simple, easy to use, look like a security app, trust,

```html
<!DOCTYPE html>
<html lang="en">
<head>
<meta charset="utf-8">
<title>vantaline7 – onboarding screens</title>
<link rel="stylesheet" href="https://fonts.googleapis.com/css2?family=Lato:wght@400;700&display=swap">
<style>
  :root {
    --canvas: #ffffff;
    --teal: #2ed3c6;
    --magenta: #ea0f77;
    --screen: #ffffff;
    --ink: #2b2b2b;
    --muted: #b4b4b4;
    --mint-soft: #e9fbf9;
    --mint: #c9f5f0;
    --btn-start: #66ddf5;
    --btn-end: #22e5d2;
  }
  * { box-sizing: border-box; margin: 0; padding: 0; }
  html, body { width: 1200px; height: 720px; overflow: hidden; }
  body {
    position: relative;
    background: var(--canvas);
    font-family: "Lato", sans-serif;
    color: var(--ink);
  }
  .bubble { position: absolute; border-radius: 50%; }
  .bubble--teal-large { left: -188px; top: -188px; width: 552px; height: 552px; background: var(--teal); }
  .bubble--pink-top { left: 644px; top: 36px; width: 216px; height: 216px; background: var(--magenta); }
  .bubble--teal-small { left: 354px; top: 460px; width: 200px; height: 200px; background: var(--teal); }
  .bubble--pink-large { left: 828px; top: 410px; width: 600px; height: 600px; background: var(--magenta); }

  .screen {
    position: absolute;
    top: 97px;
    width: 243px;
    height: 527px;
    background: var(--screen);
    box-shadow: 0 10px 40px rgba(60, 120, 120, 0.12);
  }
  .screen--register { left: 210px; }
  .screen--updates { left: 478px; }
  .screen--alarm { left: 745px; }

  .status-bar {
    position: absolute;
    top: 14px; left: 17px; right: 17px;
    display: flex; justify-content: space-between; align-items: center;
    font-size: 8px; font-weight: 700;
  }
  .status-bar svg { display: block; }

  .illustration {
    position: absolute;
    left: 28px; top: 103px;
    width: 187px; height: 168px;
    border-radius: 60px 40px 70px 50px;
    background: radial-gradient(circle at 50% 55%, var(--mint) 0%, var(--mint-soft) 70%, rgba(233,251,249,0) 100%);
  }
  .title {
    position: absolute;
    top: 300px; left: 0; right: 0;
    text-align: center;
    font-size: 15.5px; font-weight: 400;
  }
  .caption {
    position: absolute;
    top: 325px; left: 0; right: 0;
    text-align: center;
    font-size: 7.5px; line-height: 11px;
    color: var(--muted);
  }
  .next-button {
    position: absolute;
    left: 45px; top: 422px;
    width: 151px; height: 43px;
    border: 0;
    background: linear-gradient(90deg, var(--btn-start), var(--btn-end));
    color: #fff;
    font-family: "Lato", sans-serif;
    font-size: 10px; font-weight: 700;
  }
</style>
</head>
<body>
  <div class="bubble bubble--teal-large"></div>
  <div class="bubble bubble--pink-top"></div>
  <div class="bubble bubble--teal-small"></div>
  <div class="bubble bubble--pink-large"></div>

  <section class="screen screen--register">
    <div class="status-bar">
      <span>9:41</span>
      <svg width="44" height="8" viewBox="0 0 44 8" aria-hidden="true">
        <rect x="0" y="5" width="2" height="3" fill="#111"/><rect x="3" y="3.5" width="2" height="4.5" fill="#111"/><rect x="6" y="2" width="2" height="6" fill="#111"/><rect x="9" y="0.5" width="2" height="7.5" fill="#111"/>
        <path d="M15 3.2a6 6 0 0 1 8 0l-1 1.1a4.5 4.5 0 0 0-6 0z M17 5.3a3 3 0 0 1 4 0L19 7.5z" fill="#111"/>
        <rect x="29" y="1" width="12" height="6" rx="1.5" fill="#111"/><rect x="42" y="3" width="1.2" height="2" fill="#111"/>
      </svg>
    </div>
    <div class="illustration" role="img" aria-label="Illustration: person leaping beside a large phone showing a green confirmation tick"></div>
    <h2 class="title">Easy Registration</h2>
    <p class="caption">ed ut perspiciatis unde omnis<br>iste natus error</p>
    <button class="next-button">Next</button>
  </section>

  <section class="screen screen--updates">
    <div class="status-bar">
      <span>9:41</span>
      <svg width="44" height="8" viewBox="0 0 44 8" aria-hidden="true">
        <rect x="0" y="5" width="2" height="3" fill="#111"/><rect x="3" y="3.5" width="2" height="4.5" fill="#111"/><rect x="6" y="2" width="2" height="6" fill="#111"/><rect x="9" y="0.5" width="2" height="7.5" fill="#111"/>
        <path d="M15 3.2a6 6 0 0 1 8 0l-1 1.1a4.5 4.5 0 0 0-6 0z M17 5.3a3 3 0 0 1 4 0L19 7.5z" fill="#111"/>
        <rect x="29" y="1" width="12" height="6" rx="1.5" fill="#111"/><rect x="42" y="3" width="1.2" height="2" fill="#111"/>
      </svg>
    </div>
    <div class="illustration" role="img" aria-label="Illustration: people with laptops and tablets around chat bubbles and message windows"></div>
    <h2 class="title">Get Updated</h2>
    <p class="caption">ed ut perspiciatis unde omnis<br>iste natus error</p>
    <button class="next-button">Next</button>
  </section>

  <section class="screen screen--alarm">
    <div class="status-bar">
      <span>9:41</span>
      <svg width="44" height="8" viewBox="0 0 44 8" aria-hidden="true">
        <rect x="0" y="5" width="2" height="3" fill="#111"/><rect x="3" y="3.5" width="2" height="4.5" fill="#111"/><rect x="6" y="2" width="2" height="6" fill="#111"/><rect x="9" y="0.5" width="2" height="7.5" fill="#111"/>
        <path d="M15 3.2a6 6 0 0 1 8 0l-1 1.1a4.5 4.5 0 0 0-6 0z M17 5.3a3 3 0 0 1 4 0L19 7.5z" fill="#111"/>
        <rect x="29" y="1" width="12" height="6" rx="1.5" fill="#111"/><rect x="42" y="3" width="1.2" height="2" fill="#111"/>
      </svg>
    </div>
    <div class="illustration" role="img" aria-label="Illustration: hand holding a phone showing a magenta alarm shield button"></div>
    <h2 class="title">Trigger alarm</h2>
    <p class="caption">ed ut perspiciatis unde omnis<br>iste natus error</p>
    <button class="next-button">Next</button>
  </section>
</body>
</html>
```